Business Card Design Project

we are a new company , see www.chatbridgeflow.com
we also have a concurrent flyer deign competition so you may also wish to enter that.
We provide live customer support services for websites.
We cater for mainly european market.
info for card:
Martin Colbrook
Director
p: +353 (0)90 517 2861
f: +353 (0)90 517 2872
m: +353 (0)86 908 4523
e: martin@chatbridgeflow.com
w: www.chatbridgeflow.com
The card does not have to use the exact colour on the website but should ahve something of the general feel of it. It should have modern corporate feel without brash coulours. we will upload the logo and card should be standard european size 85x55mm
Target Market(s)
Online business owners
Industry/Entity Type
Business
Look and feel
Each slider illustrates characteristics of the customer's brand and the style your logo design should communicate.

```html
<!DOCTYPE html>
<html lang="en">
<head>
<meta charset="utf-8">
<title>ChatBridge Flow – Business Card</title>
<link rel="stylesheet" href="https://fonts.googleapis.com/css2?family=Open+Sans:wght@400;600;800&display=swap">
<style>
  :root {
    --backdrop: #e9e9e9;
    --blue-light: #3a97c9;
    --blue-deep: #1c6596;
    --silver-light: #fbfbfb;
    --silver-mid: #d9dadb;
    --silver-dark: #bfc1c3;
    --paper: #ffffff;
    --ink: #2e2e2e;
    --logo-grey: #55585b;
    --name-blue: #2a78ad;
    --rule: #9a9ea2;
  }
  * { box-sizing: border-box; margin: 0; padding: 0; }
  html, body { width: 1200px; height: 951px; overflow: hidden; }
  body {
    background: var(--backdrop);
    font-family: "Open Sans", Arial, sans-serif;
    position: relative;
  }
  .card {
    position: absolute;
    width: 520px;
    height: 336px;
    border-radius: 20px;
    overflow: hidden;
    box-shadow: 0 10px 28px rgba(0,0,0,0.22);
  }
  /* Front */
  .card-front {
    left: 90px; top: 90px;
    background: radial-gradient(ellipse at 45% 40%, var(--blue-light) 0%, var(--blue-deep) 85%);
    display: flex; align-items: center; justify-content: center;
  }
  .wordmark {
    display: flex; align-items: center; gap: 14px;
    font-weight: 800;
    font-size: 44px;
    letter-spacing: 0.5px;
    color: #ffffff;
  }
  .wordmark-square {
    width: 26px; height: 26px;
    background: currentColor;
  }
  /* Back */
  .card-back {
    left: 590px; top: 525px;
    background: var(--paper);
  }
  .back-band {
    position: absolute; left: 0; top: 0; width: 100%; height: 150px;
    background: linear-gradient(180deg, var(--silver-light) 0%, var(--silver-mid) 70%, var(--silver-dark) 100%);
    display: flex; align-items: center; justify-content: center;
  }
  .back-band .wordmark { color: var(--logo-grey); font-size: 36px; }
  .back-band .wordmark-square { width: 22px; height: 22px; }
  .band-notch {
    position: absolute; left: 296px; top: 149px;
  }
  .contact-list {
    position: absolute; right: 218px; top: 200px;
    list-style: none;
    font-size: 12.5px; line-height: 17px;
    color: var(--ink);
  }
  .divider {
    position: absolute; left: 318px; top: 196px;
    width: 1px; height: 92px; background: var(--rule);
  }
  .person {
    position: absolute; left: 334px; top: 232px;
    text-align: right; width: 150px;
  }
  .person-name { color: var(--name-blue); font-size: 18px; font-weight: 400; line-height: 22px; text-align: left; }
  .person-role { color: var(--ink); font-size: 12.5px; font-weight: 600; margin-top: 2px; }
</style>
</head>
<body>
  <section class="card card-front" aria-label="Card front">
    <div class="wordmark"><span class="wordmark-square"></span>ChatBridge Flow</div>
  </section>

  <section class="card card-back" aria-label="Card back">
    <div class="back-band">
      <div class="wordmark"><span class="wordmark-square"></span>ChatBridge Flow</div>
    </div>
    <svg class="band-notch" width="22" height="12" viewBox="0 0 22 12" aria-hidden="true">
      <polygon points="0,0 22,0 11,11" fill="#bfc1c3"/>
    </svg>
    <ul class="contact-list">
      <li>p: +353 (0)90 517 2861</li>
      <li>m: +353 (0)86 908 4523</li>
      <li>e: martin@chatbridgeflow.com</li>
      <li>w: www.chatbridgeflow.com</li>
    </ul>
    <div class="divider"></div>
    <div class="person">
      <div class="person-name">Martin Colbrook</div>
      <div class="person-role">Director</div>
    </div>
  </section>
</body>
</html>
```